Corrindale Planners, LLC Stationary

Corrindale Planners, LLC is a new financial planning and consulting company. We are looking for designs on business cards, letterhead, envelopes, and anything else that would be useful. Our preference for business card design is two sided. We are looking for a professional and clean look with incorporating the logo and patriotic feel. Thank you to all who participate and good luck!

```html
<!DOCTYPE html>
<html lang="en">
<head>
<meta charset="utf-8">
<title>Corrindale Planners, LLC – Letterhead</title>
<link rel="stylesheet" href="https://fonts.googleapis.com/css2?family=Open+Sans:wght@400;600&display=swap">
<style>
  :root {
    --navy: #143d6b;
    --red: #c8222b;
    --paper: #ffffff;
    --backdrop: #8e8f92;
    --ink: #2b2b2b;
    --watermark: #f4f4f4;
  }
  * { box-sizing: border-box; margin: 0; padding: 0; }
  html, body { width: 1200px; height: 1200px; overflow: hidden; }
  body {
    background: var(--backdrop);
    font-family: "Open Sans", Arial, sans-serif;
    position: relative;
  }
  .letterhead {
    position: absolute;
    left: 175px;
    top: 50px;
    width: 850px;
    height: 1100px;
    background: var(--paper);
    overflow: hidden;
  }
  .top-band {
    position: absolute;
    top: 0; left: 0; right: 0;
    height: 16px;
    background: var(--navy);
  }
  .bottom-band {
    position: absolute;
    bottom: 0; left: 0; right: 0;
    height: 30px;
    background: var(--red);
  }
  .brand {
    position: absolute;
    top: 62px;
    right: 60px;
    display: flex;
    flex-direction: column;
    align-items: flex-end;
  }
  .brand-row {
    display: flex;
    align-items: center;
    gap: 10px;
  }
  .brand-mark {
    width: 14px;
    height: 14px;
    background: var(--red);
    border-radius: 50%;
  }
  .brand-name {
    font-weight: 600;
    font-size: 26px;
    letter-spacing: 0.04em;
    color: var(--navy);
    text-transform: uppercase;
    line-height: 1;
  }
  .brand-tagline {
    margin-top: 8px;
    padding-top: 5px;
    border-top: 1px solid var(--red);
    font-size: 8.5px;
    letter-spacing: 0.22em;
    color: var(--navy);
    text-transform: uppercase;
  }
  .watermark {
    position: absolute;
    top: 50%;
    left: 50%;
    transform: translate(-50%, -50%);
    font-weight: 600;
    font-size: 96px;
    letter-spacing: 0.04em;
    color: var(--watermark);
    white-space: nowrap;
    text-transform: uppercase;
  }
  .contact {
    position: absolute;
    left: 60px;
    bottom: 52px;
    display: grid;
    grid-template-columns: auto auto;
    column-gap: 26px;
    row-gap: 8px;
    font-size: 12px;
    color: var(--ink);
  }
  .contact-item {
    display: flex;
    align-items: center;
    gap: 8px;
  }
  .contact-icon {
    width: 14px;
    height: 14px;
    flex: none;
  }
</style>
</head>
<body>
  <main class="letterhead">
    <div class="top-band"></div>

    <header class="brand">
      <div class="brand-row">
        <span class="brand-mark"></span>
        <span class="brand-name">Corrindale Planners, LLC</span>
      </div>
      <div class="brand-tagline">Financial Planning and Consulting</div>
    </header>

    <div class="watermark" aria-hidden="true">Corrindale</div>

    <footer class="contact">
      <div class="contact-item">
        <svg class="contact-icon" viewBox="0 0 14 14" aria-label="Phone">
          <rect width="14" height="14" rx="2" fill="#143d6b"/>
          <path d="M4.2 3.2l1.4 0 .7 2-1 .8a5 5 0 0 0 2.7 2.7l.8-1 2 .7v1.4c0 .5-.4.9-.9.9A7 7 0 0 1 3.3 4.1c0-.5.4-.9.9-.9z" fill="#fff"/>
        </svg>
        <span>+1 555-014-2290</span>
      </div>
      <div class="contact-item">
        <svg class="contact-icon" viewBox="0 0 14 14" aria-label="Address">
          <rect width="14" height="14" rx="2" fill="#143d6b"/>
          <path d="M7 2.8a3 3 0 0 1 3 3c0 2.2-3 5.4-3 5.4S4 8 4 5.8a3 3 0 0 1 3-3z" fill="#fff"/>
          <circle cx="7" cy="5.8" r="1.1" fill="#143d6b"/>
        </svg>
        <span>418 Alder Ridge Ave # 210, Brookfield, GA 30000, USA</span>
      </div>
      <div class="contact-item">
        <svg class="contact-icon" viewBox="0 0 14 14" aria-label="Email">
          <rect width="14" height="14" rx="2" fill="#143d6b"/>
          <rect x="3" y="4.2" width="8" height="5.6" fill="#fff"/>
          <path d="M3 4.2l4 3.2 4-3.2" fill="none" stroke="#143d6b" stroke-width="0.9"/>
        </svg>
        <span>info@CorrindalePlanners.com</span>
      </div>
      <div class="contact-item">
        <svg class="contact-icon" viewBox="0 0 14 14" aria-label="Website">
          <rect width="14" height="14" rx="2" fill="#143d6b"/>
          <circle cx="7" cy="7" r="3.6" fill="none" stroke="#fff" stroke-width="0.9"/>
          <path d="M3.4 7h7.2M7 3.4c-1.6 2-1.6 5.2 0 7.2M7 3.4c1.6 2 1.6 5.2 0 7.2" fill="none" stroke="#fff" stroke-width="0.8"/>
        </svg>
        <span>www.CorrindalePlanners.com</span>
      </div>
    </footer>

    <div class="bottom-band"></div>
  </main>
</body>
</html>
```